Kleine Website f. Unternehmensdarstellung
Zielgruppe
Geschäftsführer, Marketing & Sales Manager asiatischer Konzerne.
Aufgabenstellung
Wir sind eine Consulting und Handelsagentur mit überwiegend internationaler Kundschaft (Asien 70%).
Für einen Webauftritt, ca. 8 Seiten, haben wir eine Powerpoint Vorlage erstellt, diese zeigt nur die Inhalte. Wir benötigen nun daraus eine Website, haben eigenen Webspace, eigener Server bei Hostquelle. Wir stellen uns als Hintergrundbild auf der Frontpage Hongkong vor. Keine Flash videos oder audio einbindung ! Sprache Englisch, die Texte sollten von uns leicht editierbar sein, falls mal Anpassungen gemacht werden müssen.

```html
<!DOCTYPE html>
<html lang="en">
<head>
<meta charset="utf-8">
<title>Veltaro Group</title>
<link rel="stylesheet" href="https://fonts.googleapis.com/css2?family=Open+Sans:wght@400;600;700&display=swap">
<style>
  :root {
    --night-top: #0b0c10;
    --night-mid: #1c1a20;
    --night-glow: #4a3f35;
    --card: #ffffff;
    --ink: #111111;
    --body: #333333;
    --link: #1a44b8;
    --header-text: #ffffff;
    --footer-text: #8c8c8c;
    --footer-copy: #7a7a7a;
  }
  * { box-sizing: border-box; margin: 0; padding: 0; }
  html, body { width: 1200px; height: 696px; overflow: hidden; background: #000; }
  body { font-family: "Open Sans", Verdana, sans-serif; color: var(--body); }

  .page { position: relative; width: 1200px; height: 696px; overflow: hidden; }

  .cityscape {
    position: absolute; inset: 0;
    background:
      radial-gradient(ellipse 70% 30% at 50% 68%, rgba(120,95,70,.55), transparent 70%),
      radial-gradient(ellipse 40% 35% at 10% 40%, rgba(150,150,160,.25), transparent 70%),
      linear-gradient(180deg, var(--night-top) 0%, var(--night-mid) 45%, var(--night-glow) 72%, #151313 88%, #050505 100%);
  }

  .site-header { position: absolute; left: 0; top: 0; width: 1200px; height: 110px; }
  .welcome {
    position: absolute; left: 198px; top: 17px;
    font-size: 19px; font-weight: 400; color: var(--header-text);
  }
  .brand {
    position: absolute; left: 713px; top: 14px;
    display: flex; align-items: center; gap: 10px;
    font-size: 27px; font-weight: 700; letter-spacing: 4px; color: var(--header-text);
  }
  .brand-mark { width: 20px; height: 20px; background: var(--header-text); }
  .tagline {
    position: absolute; left: 0; top: 76px; width: 1200px; text-align: center;
    font-size: 18px; color: #eeeeee;
  }

  .segment {
    position: absolute; width: 394px;
    background: var(--card); border-radius: 6px;
    padding: 16px 22px 0 22px;
  }
  .segment h2 {
    font-size: 16px; font-weight: 400; color: var(--ink); margin-bottom: 9px; letter-spacing: .2px;
  }
  .segment p { font-size: 11px; line-height: 18px; margin-bottom: 8px; }
  .segment ul { list-style: none; margin-bottom: 4px; }
  .segment li {
    position: relative; font-size: 11px; line-height: 19px; padding-left: 19px;
  }
  .segment li::before {
    content: ""; position: absolute; left: 3px; top: 6px;
    width: 7px; height: 7px; border-radius: 50%; background: #333;
  }
  .more {
    position: absolute; right: 25px; bottom: 8px;
    font-size: 11px; color: var(--link); text-decoration: none;
  }

  .opto        { left: 197px; top: 119px; height: 158px; }
  .agency      { left: 197px; top: 290px; height: 121px; }
  .consultancy { left: 197px; top: 425px; height: 201px; }
  .financing   { left: 609px; top: 119px; height: 158px; }
  .trouble     { left: 609px; top: 290px; height: 172px; }
  .mna         { left: 609px; top: 475px; height: 151px; }

  .site-footer { position: absolute; left: 0; top: 640px; width: 1200px; text-align: center; }
  .footer-nav { display: flex; justify-content: center; gap: 27px; font-size: 10px; }
  .footer-nav a { color: var(--footer-text); text-decoration: none; }
  .copyright { margin-top: 7px; font-size: 10px; color: var(--footer-copy); }
</style>
</head>
<body>
<div class="page">
  <div class="cityscape" role="img" aria-label="Hong Kong harbour skyline at night with lit skyscrapers and searchlights"></div>

  <header class="site-header">
    <h1 class="welcome">Welcome to the Veltaro Group...</h1>
    <div class="brand"><span class="brand-mark"></span>VELTARO</div>
    <p class="tagline">Our business segments cover quite an area, please select your piont of interest</p>
  </header>

  <section class="segment opto">
    <h2>Optoelectronics / Semiconductors</h2>
    <p>We offer an outstanding service to our customers. Based on our 30 years market experience, we have unrivaled skillsets to increase our customers sales volume.</p>
    <p>We differentiate between Consultancy and Agency business models.</p>
  </section>

  <section class="segment agency">
    <h2>Agency</h2>
    <p>We buy, import and sell optoelectronic semiconductors throughout our salesnetwork, covering Europe and Scandinavia.</p>
    <a class="more" href="#">More...(2)</a>
  </section>

  <section class="segment consultancy">
    <h2>Consultancy</h2>
    <p>Consulting means, understanding what the customers want. If you prefer to enter a market silently, we are the right choice.</p>
    <p>This can be:<br>Setup of an european sales network Identifying M&amp;A targets, proxy negotiations Market analysis and recommendations</p>
    <a class="more" href="#">More...(2)</a>
  </section>

  <section class="segment financing">
    <h2>Technology Financing</h2>
    <ul>
      <li>You or your company have an outstanding product or idea</li>
      <li>For the extension of market shares you need support</li>
      <li>You want to retract from Europe and sell your assets</li>
    </ul>
    <p>This is exactly, what we like and where we can add enormous power.</p>
    <a class="more" href="#">More...(4)</a>
  </section>

  <section class="segment trouble">
    <h2>Troubleshooting</h2>
    <ul>
      <li>Your project runs out of bounds</li>
      <li>Pricing, quality and milestones are not met by the vendors</li>
      <li>Prototype works but the transition to industrial usage stucks</li>
      <li>You desparately need a second source for mission critical parts</li>
    </ul>
    <p>This is exactly, what we like and where we can add enormous power.</p>
    <a class="more" href="#">More...(5)</a>
  </section>

  <section class="segment mna">
    <h2>M &amp; A , the silent service</h2>
    <ul>
      <li>You understand the time to market entrance issue</li>
      <li>You want to prove and identify targets for aquisition</li>
      <li>You need a proxy to make first contacts and evaluate</li>
      <li>You just need a concise market overview about your competitors</li>
    </ul>
    <a class="more" href="#">More...(6)</a>
  </section>

  <footer class="site-footer">
    <nav class="footer-nav">
      <a href="#">Home</a>
      <a href="#">Agency</a>
      <a href="#">Consultancy</a>
      <a href="#">Technology Finance</a>
      <a href="#">Troubleshooting</a>
      <a href="#">M&amp;A Silent Service</a>
    </nav>
    <p class="copyright">Copyright 2010. Veltaro Group. All Rights Reserved.</p>
  </footer>
</div>
</body>
</html>
```